UI/UX Re-Do for Velmora - a free to use project management platform for desktop and mobile.

UI/UX Re-Do for Velmora
Velmora is a free to use project management platform for desktop and mobile.
We are looking for help with our UI/UX re-design.
As of now the platform is totally functional.
The problem is around flow and look. We want VM to become something that any one can use to manage and even socialize any project. A project can be something work related like organizing a team around a software build, marketing campaign, shared client file space, etc... In fact, most of our current members are using VM for just such work projects.
We also see a project as planning a wedding, organizing a group trip, a simple to-do list, organizing a kids sports team, and so on...
To become a platform that people will use in their work and personal life we first need to become more intuitive and friendly - while maintaining advanced functionality for more advanced needs.
We need help to beautify, streamline, and simplify - while keeping all the functions.
The quickest way to understand VM, and our current issues is this short video:
https://vidshare-example.net/Kq8TzRw2mLp
For sure see this link for the entire most recent description AND images:
https://velmoraapp-example.com/?p=HtrwN4YcZsD
The best way to understand VM is to actually use it:
https://velmoraapp-example.com
Should you choose to take a run at improving VM here are the details:
Please focus your ideas for mobile, it's where we have the biggest issues.
Feel free to get outside the box.
Avoid swipe oriented designs.
Feel free to focus on ideas over polished outputs.
Use any tool you like, PS, hand drawing, written description if you think that works best.
(FYI - we use mostly use Google Presentation docs internally)
Point is illustration of ideas over tool choice.
Feel free to:
Create something totally new
And/or riff on what we have now
And/or riff on the new design we are considering (see images below)
|||
If we go the direction of the images/designs below the idea is to give people options on how they see/experience VM.
Just below is what we are calling Base Mode. This is a more basic and simple flow. Probably a default to keep new users feeling comfortable at the start.
<img src="https://img.picvault-example.net/8tqWLbN.jpg" style="width: 100%;">
https://img.picvault-example.net/8tqWLbN.jpg
|||
We are calling this optional view Atlas Mode. It is more advanced and can show all project, goal(renamed 'milestones') at the same time. This is more of a paint job on the current design.
<img src="https://img.picvault-example.net/mvdHRsJ.jpg" style="width: 100%;">
https://img.picvault-example.net/mvdHRsJ.jpg
|||
If you're submitting please let us know if you can also do the PS files for dev.
Not required, but once we nail down the concepts we want someone to hone in the PS files.
As an optional bonus we will also be giving credit to you/your company in VM.
Let us know if you do or don't want that.
We are excited to see your work!!
<img src=" " style="width: 100%;">
Target Market(s)
Anyone who needs to organize any project, big or small. The key is to make a super friendly user experience for new users while retaining advanced functions.

```html
<!DOCTYPE html>
<html lang="en">
<head>
<meta charset="utf-8">
<title>Velmora – Project Overview</title>
<link rel="stylesheet" href="https://fonts.googleapis.com/css2?family=Montserrat:wght@400;500;600&display=swap">
<style>
  :root {
    --bg: #f5f5f5;
    --surface: #ffffff;
    --ink: #111111;
    --ink-muted: #8d8d8d;
    --ink-soft: #6b6b6b;
    --tab-idle: #a3a3a3;
    --accent: #8b5cb1;
    --teal: #4fb4c8;
    --badge: #1f86d9;
    --fab-red: #ee1c25;
    --divider: #9a9a9a;
    --avatar: #d8d3cf;
  }
  * { box-sizing: border-box; margin: 0; padding: 0; }
  html, body { width: 675px; height: 1200px; overflow: hidden; }
  body {
    position: relative;
    background: var(--bg);
    font-family: "Montserrat", sans-serif;
    color: var(--ink);
  }
  .app-header {
    position: absolute; left: 0; top: 0; width: 675px; height: 218px;
    background: var(--surface);
    box-shadow: 0 2px 6px rgba(0,0,0,0.08);
  }
  .back-button { position: absolute; left: 32px; top: 54px; width: 40px; height: 36px; }
  .project-title {
    position: absolute; left: 148px; top: 57px;
    font-size: 27px; font-weight: 500; letter-spacing: 0.3px;
  }
  .avatar {
    position: absolute; left: 536px; top: 20px; width: 110px; height: 110px;
    border-radius: 50%;
    background: radial-gradient(circle at 50% 40%, #e9d2c4 0%, var(--avatar) 55%, #2f3a45 100%);
  }
  .avatar-badge {
    position: absolute; left: 618px; top: 25px; width: 30px; height: 30px;
    border-radius: 50%; background: var(--badge); color: #fff;
    font-size: 15px; font-weight: 500;
    display: flex; align-items: center; justify-content: center;
  }
  .tabs { position: absolute; left: 0; top: 168px; width: 675px; height: 50px; }
  .tab {
    position: absolute; top: 0; width: 225px; text-align: center;
    font-size: 27px; font-weight: 500; color: var(--tab-idle);
  }
  .tab--active { color: var(--accent); }
  .tab-indicator {
    position: absolute; left: 0; bottom: 0; width: 225px; height: 4px; background: var(--accent);
  }
  .stats-card {
    position: absolute; left: 0; top: 238px; width: 675px; height: 270px;
    background: var(--surface);
    box-shadow: 0 6px 14px rgba(0,0,0,0.12);
  }
  .progress-ring { position: absolute; left: 94px; top: 276px; width: 186px; height: 186px; }
  .progress-value {
    position: absolute; left: 94px; top: 339px; width: 186px; text-align: center;
    font-size: 43px; font-weight: 400; color: var(--teal); line-height: 1;
  }
  .progress-label {
    position: absolute; left: 94px; top: 387px; width: 186px; text-align: center;
    font-size: 12.5px; font-weight: 500; color: var(--ink-soft); letter-spacing: 0.3px;
  }
  .card-divider { position: absolute; left: 338px; top: 261px; width: 1px; height: 225px; background: var(--divider); }
  .stat { position: absolute; left: 411px; }
  .stat-number { font-size: 45px; font-weight: 500; line-height: 1; }
  .stat-label { margin-top: 6px; font-size: 12.5px; font-weight: 500; color: var(--ink-soft); letter-spacing: 0.2px; }
  .meta { position: absolute; top: 543px; }
  .meta-label { font-size: 13.5px; color: var(--ink-muted); }
  .meta-value { margin-top: 6px; font-size: 17.5px; font-weight: 500; line-height: 33px; }
  .fab {
    position: absolute; border-radius: 50%;
    display: flex; align-items: center; justify-content: center;
  }
  .fab--calendar {
    left: 551px; top: 957px; width: 86px; height: 86px; background: var(--surface);
    box-shadow: 0 4px 14px rgba(238,28,37,0.25);
  }
  .fab--add {
    left: 540px; top: 1058px; width: 108px; height: 108px; background: var(--fab-red);
    box-shadow: 0 6px 14px rgba(238,28,37,0.3);
  }
</style>
</head>
<body>
  <header class="app-header">
    <svg class="back-button" viewBox="0 0 40 36" aria-label="Back">
      <path d="M38 18H4M18 3L3 18l15 15" fill="none" stroke="#707070" stroke-width="3"/>
    </svg>
    <h1 class="project-title">Project Title</h1>
    <div class="avatar" role="img" aria-label="Profile photo of the signed-in user"></div>
    <div class="avatar-badge">5</div>
    <nav class="tabs">
      <div class="tab tab--active" style="left:0">Overview</div>
      <div class="tab" style="left:243px">Tasks</div>
      <div class="tab" style="left:468px">Files</div>
      <div class="tab-indicator"></div>
    </nav>
  </header>

  <section class="stats-card">
  </section>
  <svg class="progress-ring" viewBox="0 0 186 186" aria-hidden="true">
    <defs>
      <radialGradient id="ringFace" cx="40%" cy="35%" r="70%">
        <stop offset="0" stop-color="#ffffff"/>
        <stop offset="1" stop-color="#e3e3e3"/>
      </radialGradient>
      <filter id="ringShadow" x="-20%" y="-20%" width="140%" height="150%">
        <feDropShadow dx="0" dy="6" stdDeviation="5" flood-color="#000" flood-opacity="0.25"/>
      </filter>
    </defs>
    <circle cx="93" cy="93" r="82" fill="url(#ringFace)" filter="url(#ringShadow)"/>
    <circle cx="93" cy="93" r="82" fill="none" stroke="#4fb4c8" stroke-width="5"
      stroke-dasharray="319.4 515.2" transform="rotate(-90 93 93)"/>
  </svg>
  <div class="progress-value">62%</div>
  <div class="progress-label">COMPLETED</div>
  <div class="card-divider"></div>
  <div class="stat" style="top:296px">
    <div class="stat-number">22</div>
    <div class="stat-label">TASKS COMPLETED</div>
  </div>
  <div class="stat" style="top:397px">
    <div class="stat-number">06</div>
    <div class="stat-label">TASKS IN PROGRESS</div>
  </div>

  <div class="meta" style="left:60px">
    <div class="meta-label">Project Manager</div>
    <div class="meta-value">Reid Halvorsen</div>
  </div>
  <div class="meta" style="left:338px">
    <div class="meta-label">Duration</div>
    <div class="meta-value">9/20/2017<br>-<br>9/27/2017</div>
  </div>

  <div class="fab fab--calendar" aria-label="Calendar">
    <svg width="36" height="36" viewBox="0 0 36 36" aria-hidden="true">
      <rect x="2" y="6" width="32" height="28" rx="2" fill="#d3dbe0"/>
      <rect x="2" y="6" width="32" height="8" rx="2" fill="#ee3b3b"/>
      <rect x="9" y="2" width="3" height="8" rx="1.5" fill="#9aa5ad"/>
      <rect x="24" y="2" width="3" height="8" rx="1.5" fill="#9aa5ad"/>
      <g fill="#8e9aa3">
        <rect x="7" y="17" width="4" height="3"/><rect x="13" y="17" width="4" height="3"/><rect x="19" y="17" width="4" height="3"/><rect x="25" y="17" width="4" height="3"/>
        <rect x="7" y="22" width="4" height="3"/><rect x="13" y="22" width="4" height="3"/><rect x="19" y="22" width="4" height="3"/><rect x="25" y="22" width="4" height="3"/>
        <rect x="7" y="27" width="4" height="3"/><rect x="13" y="27" width="4" height="3"/><rect x="19" y="27" width="4" height="3"/>
      </g>
    </svg>
  </div>
  <div class="fab fab--add" aria-label="Add">
    <svg width="30" height="30" viewBox="0 0 30 30" aria-hidden="true">
      <path d="M15 2v26M2 15h26" stroke="#fff" stroke-width="3"/>
    </svg>
  </div>
</body>
</html>
```